Business Card Design for Toriven

I've already got the logo, but I'd like to see some interesting designs.

I don't want anything to complex. I like it simple,yet innovative, like the logo.

My business is System Administration for small to medium size businesses, so that will be my main target audience.
Updates

hey all, the png has been uploaded.

Hey all,

If you are submitting the back side of the card, I'd like the top bit of the card to be Toriven Solutions and the logo, the bottom of the card the website, with a white background.

The middle I'd like to leave blank for a quote that will be printed on each card.

Thanks!

Dale

Industry/Entity Type

Business

```html
<!DOCTYPE html>
<html lang="en">
<head>
<meta charset="utf-8">
<title>Toriven Solutions – Business Card</title>
<link rel="stylesheet" href="https://fonts.googleapis.com/css2?family=Arimo:wght@400;700&family=Roboto+Condensed:wght@500&display=swap">
<style>
  :root {
    --brand-blue: #1b78b6;
    --ink: #231f20;
    --ink-soft: #58595b;
    --bar-grey: #4d4d4f;
    --paper-light: #ffffff;
    --paper-shade: #dedede;
  }
  * { margin: 0; padding: 0; box-sizing: border-box; }
  html, body { width: 1200px; height: 709px; overflow: hidden; background: #ffffff; }
  .card {
    position: relative;
    width: 1200px;
    height: 709px;
    overflow: hidden;
    background: linear-gradient(120deg, var(--paper-light) 0%, var(--paper-light) 45%, #f1f1f1 75%, var(--paper-shade) 100%);
    font-family: "Arimo", Arial, sans-serif;
    color: var(--ink);
  }
  .brand-mark { position: absolute; left: 344px; top: 26px; }
  .brand-name {
    position: absolute;
    left: 550px;
    top: 70px;
    font-size: 82px;
    font-weight: 700;
    line-height: 1;
    color: var(--brand-blue);
    letter-spacing: -1px;
  }
  .brand-tagline {
    position: absolute;
    left: 554px;
    top: 153px;
    font-size: 24px;
    font-weight: 700;
    line-height: 1;
    color: var(--brand-blue);
    letter-spacing: 14px;
  }
  .company-message {
    position: absolute;
    left: 0;
    width: 1200px;
    top: 204px;
    text-align: center;
    font-size: 46px;
    font-weight: 700;
    line-height: 1;
  }
  .person-name {
    position: absolute;
    left: 69px;
    top: 311px;
    font-size: 37px;
    font-weight: 700;
    line-height: 1;
    color: var(--ink-soft);
  }
  .person-role {
    position: absolute;
    left: 69px;
    top: 348px;
    font-size: 28px;
    line-height: 1;
    color: var(--ink-soft);
  }
  .contact-row { position: absolute; left: 69px; line-height: 1; }
  .contact-label {
    position: absolute;
    left: 0;
    top: 0;
    font-size: 34px;
    font-weight: 700;
    font-variant: small-caps;
    color: var(--ink-soft);
    white-space: nowrap;
  }
  .contact-colon {
    position: absolute;
    left: 150px;
    top: 0;
    font-size: 32px;
    font-weight: 700;
    color: var(--ink);
  }
  .contact-value {
    position: absolute;
    left: 183px;
    top: 6px;
    font-family: "Roboto Condensed", "Arial Narrow", sans-serif;
    font-size: 28px;
    font-weight: 500;
    color: var(--ink);
    white-space: nowrap;
  }
  .contact-value span { display: block; margin-bottom: 8px; }
  .row-phone { top: 397px; }
  .row-email { top: 444px; }
  .row-website { top: 496px; }
  .row-address { top: 545px; }
  .rule-grey {
    position: absolute;
    left: 0; top: 648px;
    width: 245px; height: 9px;
    background: var(--bar-grey);
  }
  .rule-blue {
    position: absolute;
    left: 300px; top: 648px;
    width: 900px; height: 8px;
    background: var(--brand-blue);
  }
</style>
</head>
<body>
  <main class="card">
    <svg class="brand-mark" width="156" height="156" viewBox="0 0 156 156" aria-hidden="true">
      <circle cx="78" cy="78" r="76" fill="var(--brand-blue)"/>
    </svg>
    <div class="brand-name">Toriven</div>
    <div class="brand-tagline">Solutions</div>

    <h1 class="company-message">Company Message</h1>

    <div class="person-name">Name</div>
    <div class="person-role">Designation</div>

    <div class="contact-row row-phone">
      <span class="contact-label">Phone</span><span class="contact-colon">:</span>
      <span class="contact-value">Enter phone number here</span>
    </div>
    <div class="contact-row row-email">
      <span class="contact-label">Email</span><span class="contact-colon">:</span>
      <span class="contact-value">Enter mail ID here</span>
    </div>
    <div class="contact-row row-website">
      <span class="contact-label">Website</span><span class="contact-colon">:</span>
      <span class="contact-value">Enter web address here</span>
    </div>
    <div class="contact-row row-address">
      <span class="contact-label">Address</span><span class="contact-colon">:</span>
      <span class="contact-value"><span>Address line 1</span><span>Address line 2</span></span>
    </div>

    <div class="rule-grey"></div>
    <div class="rule-blue"></div>
  </main>
</body>
</html>
```